A QUIET AMBER PRIMER ON RANKS

subtitle: AN INTRO TO SEARCH ENGINE OPTIMIZATION
background: white
dimensions: 1562x2500

Target Market(s)

Marketing professionals

Industry/Entity Type

Digital Marketing

Font styles to use
Sans Serif

Colors
ffffff
1b1b1b
3176b5

Requirements
Should not have
• Images or graphics

```html
<!DOCTYPE html>
<html lang="en">
<head>
<meta charset="utf-8">
<title>A Quiet Amber Primer on Ranks</title>
<link rel="stylesheet" href="https://fonts.googleapis.com/css2?family=Archivo:wght@300;800;900&display=swap">
<style>
  :root {
    --paper: #e8e8e7;
    --paper-band: #f6f6f5;
    --band-edge: #d2d2d1;
    --ink: #1b1b1b;
    --accent: #3176b5;
  }
  html, body {
    margin: 0;
    padding: 0;
    width: 801px;
    height: 1200px;
    overflow: hidden;
    background: #ffffff;
  }
  .cover {
    position: relative;
    width: 801px;
    height: 1200px;
    background: var(--paper);
    overflow: hidden;
  }
  .cover-art {
    position: absolute;
    inset: 0;
    width: 801px;
    height: 1200px;
    display: block;
  }
  .title-light { font-family: "Archivo", Arial, sans-serif; font-weight: 300; fill: var(--ink); }
  .title-heavy { font-family: "Archivo", Arial, sans-serif; font-weight: 800; fill: var(--ink); }
  .title-accent { font-family: "Archivo", Arial, sans-serif; font-weight: 900; fill: var(--accent); }
  .band { fill: var(--paper-band); }
  .band-edge { fill: var(--band-edge); }
</style>
</head>
<body>
  <main class="cover">
    <svg class="cover-art" viewBox="0 0 801 1200" xmlns="http://www.w3.org/2000/svg" role="img" aria-label="A Quiet Amber Primer on Ranks. An intro to search engine optimization. Author name.">
      <rect class="band" x="0" y="571" width="801" height="274"/>
      <rect class="band-edge" x="0" y="571" width="801" height="3"/>
      <rect class="band-edge" x="0" y="842" width="801" height="3"/>

      <g class="title" text-anchor="middle">
        <text class="title-heavy" x="400" y="92" font-size="52">A</text>
        <text class="title-light" x="400" y="227" font-size="150" textLength="550" lengthAdjust="spacingAndGlyphs">QUIET</text>
        <text class="title-light" x="400" y="369" font-size="155" textLength="550" lengthAdjust="spacingAndGlyphs">AMBER</text>
        <text class="title-heavy" x="400" y="512" font-size="162" textLength="545" lengthAdjust="spacingAndGlyphs">PRIMER</text>
        <text class="title-heavy" x="400" y="560" font-size="47" textLength="86" lengthAdjust="spacingAndGlyphs">ON</text>
        <text class="title-accent" x="400" y="800" font-size="245" textLength="590" lengthAdjust="spacingAndGlyphs">RANKS</text>

        <text class="title-heavy" x="400" y="923" font-size="46" textLength="593" lengthAdjust="spacingAndGlyphs">AN INTRO TO SEARCH</text>
        <text class="title-heavy" x="400" y="977" font-size="46" textLength="593" lengthAdjust="spacingAndGlyphs">ENGINE OPTIMIZATION</text>

        <text class="title-heavy" x="400" y="1144" font-size="74" textLength="642" lengthAdjust="spacingAndGlyphs">AUTHOR NAME</text>
      </g>
    </svg>
  </main>
</body>
</html>
```